BeamRangers Laser Tag party invitation

An A4 foldable to A6 party invitation that parents can fill in (either in Adobe PDF using computer, or hand written) giving party details including
1. Whose party
2. What party (eg 10th Birthday, XMas, end of term)
3. Where
4. When
5. What time - FROM __ am/pm TO __am/pm
6. RSVP name and tel

The front of the invite should incorporate drawn anime figures, pref boys and girls, and show energy, outdoors, fun, being active.
Target is for parents of 10-15 year old kids who want to use a custom invite to send out.

Back of card should have business details
Beamrangers
Mobile Laser Tag
parties * school camps * teambuilding * fundraisers * fetes
Contact Details
Marcie 0427-318-962
Troy 0439-764-213
www.beamrangers-example.com.au
bookings@beamrangers-example.com.au

Inside of card Right hand side should have a "what to bring" (blank) section
Below this section, at the bottom, should be a note
"Please wear enclosed shoes suitable for running around outside"

Target Market(s)

Parents of 10-15yr kids, predominantly boys

Industry/Entity Type

School

Requirements
Must have
• A4 foldable to A6 size, printed one side only - see attached uploaded (amateurish!) examples
Nice to have
• PDF format where user can print blank invite (and hand fill in party details) AND
PDF form where user can enter in the details on computer and have the form printed with details filled in.
Ideally would be nice if user can also choose font.

Really nice if basic design can be tweaked for boys or girls, or boys and girls (ie a mixed gender party)
Should not have
• Nothing too military / gore

```html
<!DOCTYPE html>
<html lang="en">
<head>
<meta charset="utf-8">
<title>BeamRangers Laser Tag Party Invitation</title>
<link rel="stylesheet" href="https://fonts.googleapis.com/css2?family=Audiowide&family=Black+Ops+One&family=Oswald:wght@500&family=Montserrat:wght@700&display=swap">
<style>
  :root {
    --page: #ffffff;
    --navy-deep: #14122e;
    --navy: #221d4a;
    --magenta: #b0237e;
    --pink-glow: #f05ab4;
    --violet: #5a2a7a;
    --white: #ffffff;
    --ice: #a9c9ea;
    --lilac: #9b8fe0;
    --contact-top: #8cbbe6;
    --contact-bottom: #8b8ee0;
    --art-sky: #e5796f;
    --art-mid: #b8d2e8;
    --art-deep: #4d6fb5;
  }
  * { box-sizing: border-box; margin: 0; padding: 0; }
  html, body { width: 1200px; height: 800px; overflow: hidden; background: var(--page); }

  .invitation {
    position: absolute; left: 42px; top: 2px;
    width: 1033px; height: 776px;
    display: flex;
  }
  .panel {
    position: relative; width: 50%; height: 100%; overflow: hidden;
    background:
      radial-gradient(ellipse 70% 38% at 50% 18%, rgba(240,90,180,0.85), transparent 70%),
      linear-gradient(180deg, var(--magenta) 0%, var(--violet) 30%, var(--navy) 55%, var(--navy-deep) 100%);
    color: var(--white);
    text-align: center;
  }
  .panel-rays { position: absolute; inset: 0; width: 100%; height: 100%; pointer-events: none; }

  /* Back panel */
  .brand-name {
    position: absolute; top: 52px; left: 0; right: 0;
    font-family: "Audiowide", sans-serif; font-weight: 400;
    font-size: 66px; line-height: 92px; letter-spacing: 2px;
    text-transform: uppercase; color: var(--white);
  }
  .service-title {
    position: absolute; top: 312px; left: 0; right: 0;
    font-family: "Audiowide", sans-serif; font-size: 33px; letter-spacing: 1px;
    text-transform: uppercase;
  }
  .service-list { position: absolute; top: 370px; left: 0; right: 0; list-style: none; }
  .service-list li {
    font-family: "Audiowide", sans-serif; font-size: 16px; line-height: 30px;
    letter-spacing: 2px; text-transform: uppercase;
  }
  .service-list li::before, .service-list li::after {
    content: ""; display: inline-block; width: 7px; height: 7px; border-radius: 50%;
    background: var(--white); vertical-align: middle; margin: 0 10px 4px;
  }
  .contact {
    position: absolute; top: 588px; left: 0; right: 0;
    font-family: "Oswald", sans-serif; font-weight: 500; font-size: 16px; line-height: 32px;
  }
  .contact p:nth-child(1) { color: var(--contact-top); }
  .contact p:nth-child(2), .contact p:nth-child(3) { color: #8aaee4; }
  .contact p:nth-child(4), .contact p:nth-child(5) { color: var(--contact-bottom); }

  /* Front panel */
  .invite-heading {
    position: absolute; top: 70px; left: 0; right: 0;
    font-family: "Black Ops One", sans-serif; font-size: 70px; line-height: 80px;
    letter-spacing: 3px; text-transform: uppercase; color: #f6e8f2;
  }
  .hero-art {
    position: absolute; left: 0; right: 0; top: 282px; height: 282px;
    clip-path: polygon(0 4%, 100% 12%, 100% 82%, 0 100%);
    background:
      radial-gradient(ellipse 50% 60% at 65% 55%, #f2c7b5, transparent 70%),
      linear-gradient(100deg, var(--art-sky) 0%, var(--art-mid) 45%, var(--art-deep) 100%);
  }
  .party-title {
    position: absolute; top: 574px; left: 0; right: 0;
    font-family: "Audiowide", sans-serif; font-size: 60px; line-height: 76px;
    letter-spacing: 3px; text-transform: uppercase;
  }
  .party-title .line-one { display: block; color: var(--ice); }
  .party-title .line-two { display: block; color: var(--lilac); }
  .front-web {
    position: absolute; top: 746px; left: 0; right: 0;
    font-family: "Montserrat", sans-serif; font-weight: 700; font-size: 15px; letter-spacing: 0.5px;
  }

  .fold-mark { position: absolute; left: 516px; top: 2px; width: 80px; height: 300px; }
</style>
</head>
<body>
<main class="invitation">
  <section class="panel panel-back">
    <svg class="panel-rays" viewBox="0 0 516 776" aria-hidden="true">
      <g stroke="rgba(255,220,245,0.35)" stroke-width="3">
        <line x1="258" y1="230" x2="0" y2="60"/><line x1="258" y1="230" x2="516" y2="40"/>
        <line x1="258" y1="230" x2="60" y2="0"/><line x1="258" y1="230" x2="470" y2="0"/>
        <line x1="258" y1="230" x2="0" y2="340"/><line x1="258" y1="230" x2="516" y2="330"/>
      </g>
      <g fill="rgba(255,200,240,0.22)" stroke="rgba(255,255,255,0.35)">
        <circle cx="308" cy="45" r="30"/><circle cx="330" cy="250" r="34"/>
        <circle cx="460" cy="130" r="18"/><circle cx="120" cy="270" r="14"/>
        <circle cx="20" cy="330" r="30"/><circle cx="360" cy="390" r="10"/>
      </g>
    </svg>
    <h1 class="brand-name">Beam<br>Rangers</h1>
    <h2 class="service-title">Mobile Laser Tag</h2>
    <ul class="service-list">
      <li>Parties</li><li>School Camps</li><li>Teambuilding</li><li>Fundraisers</li><li>Fetes</li>
    </ul>
    <div class="contact">
      <p>Contact Details</p>
      <p>Marcie 0427-318-962</p>
      <p>Troy 0439-764-213</p>
      <p>www.beamrangers-example.com.au</p>
      <p>bookings@beamrangers-example.com.au</p>
    </div>
  </section>

  <section class="panel panel-front">
    <svg class="panel-rays" viewBox="0 0 517 776" aria-hidden="true">
      <g stroke="rgba(255,220,245,0.35)" stroke-width="3">
        <line x1="258" y1="220" x2="0" y2="40"/><line x1="258" y1="220" x2="517" y2="50"/>
        <line x1="258" y1="220" x2="120" y2="0"/><line x1="258" y1="220" x2="420" y2="0"/>
      </g>
      <g fill="rgba(255,200,240,0.22)" stroke="rgba(255,255,255,0.35)">
        <circle cx="210" cy="45" r="28"/><circle cx="228" cy="255" r="36"/>
        <circle cx="470" cy="165" r="20"/><circle cx="60" cy="130" r="18"/>
        <circle cx="300" cy="130" r="14"/>
      </g>
    </svg>
    <h2 class="invite-heading">You are<br>invited</h2>
    <div class="hero-art" role="img" aria-label="Anime-style illustration of a young laser tag player running with energy"></div>
    <h1 class="party-title"><span class="line-one">Laser Tag</span><span class="line-two">Party</span></h1>
    <p class="front-web">www.beamrangers-example.com.au</p>
  </section>

  <svg class="fold-mark" viewBox="0 0 80 300" aria-hidden="true">
    <path d="M40 150 Q80 200 40 262 Q0 200 40 150 Z" fill="rgba(255,255,255,0.08)" stroke="rgba(255,255,255,0.4)" stroke-width="1.5"/>
  </svg>
</main>
</body>
</html>
```